Anzeigengestaltung für Apotheke
Zielgruppe
Lindmoor-Apotheke
klassische Vor Ort Apotheke, Zielgruppe ältere Menschen und Gesundheitsbewusste Menschen, die ihren Cholesterinwert wissen wollen.
Aufgabenstellung
Keine Speziellen, außer, dass unser Logo in die Anzeige integriert werden soll. Anzeige in DIN A 6 Format und sollte folgenden Inhalt haben:
Irgend ein Teaser : (Gern auch mal im Internet gucken bei anderen Apotheken)
Cholesterin- Woche vom 24.-29. Oktober
Wir messen Ihren Cholesterol Wert inklusive HDL, LDL und Gesamtcholesterin
Anmeldung erbeten bei Frau Hesse: hesse@lindmoor-apotheke.example oder unter 0761 58 72 19

```html
<!DOCTYPE html>
<html lang="de">
<head>
<meta charset="utf-8">
<title>Lindmoor-Apotheke – Cholesterinwoche</title>
<link rel="stylesheet" href="https://fonts.googleapis.com/css2?family=Roboto:wght@400;500;700&family=Caveat:wght@500&display=swap">
<style>
  :root {
    --green: #3a5f2c;
    --green-text: #46702f;
    --red: #c0202a;
    --ink: #1d1d1b;
    --grey: #dfe0dc;
    --photo-light: #eef2f4;
    --white: #ffffff;
    --page: #ffffff;
  }
  * { margin: 0; padding: 0; box-sizing: border-box; }
  html, body { width: 1200px; height: 1200px; overflow: hidden; background: var(--page); }
  body { position: relative; font-family: "Roboto", Arial, sans-serif; color: var(--ink); }

  .flyer {
    position: absolute; left: 325px; top: 230px;
    width: 538px; height: 756px;
    background: var(--white);
    box-shadow: 0 2px 10px rgba(0,0,0,.28);
    overflow: hidden;
  }
  .flyer__body {
    position: absolute; left: 0; top: 243px; width: 100%; height: 487px;
    background: var(--grey);
  }
  .flyer__footer {
    position: absolute; left: 0; bottom: 0; width: 100%; height: 26px;
    background: var(--green);
  }

  .brand {
    position: absolute; left: 34px; top: 40px;
    display: flex; align-items: center; gap: 14px;
  }
  .brand__dot {
    width: 62px; height: 62px; border-radius: 50%; background: var(--green);
  }
  .brand__name {
    font-weight: 700; font-size: 34px; color: var(--green); letter-spacing: -.3px;
  }
  .tagline {
    position: absolute; left: 230px; top: 104px; width: 280px;
    font-family: "Caveat", cursive; font-weight: 500; font-size: 34px; line-height: 30px;
    color: var(--red); text-align: right;
    transform: rotate(-7deg); transform-origin: right center;
  }

  .teaser {
    position: absolute; left: 30px; top: 210px; width: 472px; height: 96px;
    background: var(--green); color: var(--white);
    transform: rotate(-4.5deg);
    box-shadow: 0 3px 6px rgba(0,0,0,.25);
    text-align: center; padding-top: 12px;
    z-index: 2;
  }
  .teaser__title { font-weight: 700; font-size: 36px; letter-spacing: .5px; line-height: 40px; }
  .teaser__sub { font-weight: 500; font-size: 24px; line-height: 30px; }

  .offer { position: absolute; left: 0; top: 318px; width: 100%; text-align: center; z-index: 2; }
  .offer__lead { font-size: 22px; font-weight: 500; }
  .offer__name { font-size: 33px; font-weight: 500; color: var(--red); }
  .offer__dates { font-size: 21px; font-weight: 500; margin-top: 4px; }

  .checklist { position: absolute; left: 74px; top: 410px; width: 440px; list-style: none; z-index: 2; }
  .checklist__item { position: relative; padding-left: 38px; font-size: 19px; line-height: 25px; }
  .checklist__item + .checklist__item { margin-top: 20px; }
  .checklist__box { position: absolute; left: 0; top: 2px; width: 22px; height: 22px; }
  .hl { color: var(--green-text); font-weight: 500; }
  .contact-line { display: block; line-height: 26px; }

  .hero-photo {
    position: absolute; left: 0; top: 480px; width: 400px; height: 250px;
    background: linear-gradient(90deg, var(--photo-light) 0%, var(--photo-light) 55%, var(--grey) 100%);
    -webkit-mask-image: linear-gradient(180deg, transparent 0%, #000 35%);
    mask-image: linear-gradient(180deg, transparent 0%, #000 35%);
    z-index: 1;
  }

  .address {
    position: absolute; right: 40px; top: 588px; text-align: right;
    font-size: 13.5px; line-height: 20px; font-style: normal;
    z-index: 2;
  }
  .address__name { font-weight: 700; }
</style>
</head>
<body>
  <main class="flyer">
    <div class="flyer__body"></div>

    <div class="brand">
      <span class="brand__dot"></span>
      <span class="brand__name">Lindmoor-Apotheke</span>
    </div>
    <p class="tagline">Gesundheit mitten<br>in Lindmoor!</p>

    <div class="teaser">
      <p class="teaser__title">CHOLESTERIN?</p>
      <p class="teaser__sub">Kennen Sie Ihre Werte?</p>
    </div>

    <section class="offer">
      <p class="offer__lead">Unser Angebot: <span class="offer__name">Cholestrinwoche</span></p>
      <p class="offer__dates">vom 24. - 29. Oktober 2022</p>
    </section>

    <div class="hero-photo" role="img" aria-label="Foto: rotes Herz mit Stethoskop vor hellem, unscharfem Apothekenhintergrund"></div>

    <ul class="checklist">
      <li class="checklist__item">
        <svg class="checklist__box" viewBox="0 0 22 22"><rect width="22" height="22" rx="2" fill="#3a5f2c"/><path d="M5 11.5l4 4 8-9" fill="none" stroke="#fff" stroke-width="3" stroke-linecap="round" stroke-linejoin="round"/></svg>
        Wir messen Ihren <span class="hl">Cholesterol Wert</span><br>inklusive <span class="hl">HDL</span>, <span class="hl">LDL</span> und <span class="hl">Gesamtcholesterin</span>
      </li>
      <li class="checklist__item">
        <svg class="checklist__box" viewBox="0 0 22 22"><rect width="22" height="22" rx="2" fill="#3a5f2c"/><path d="M5 11.5l4 4 8-9" fill="none" stroke="#fff" stroke-width="3" stroke-linecap="round" stroke-linejoin="round"/></svg>
        <span class="hl">Anmeldung erbeten bei Frau Hesse:</span>
        <span class="contact-line">hesse@lindmoor-apotheke.example oder</span>
        <span class="contact-line">unter 0761 58 72 19</span>
      </li>
    </ul>

    <address class="address">
      <span class="address__name">Lindmoor-Apotheke</span><br>
      Mühlweg 12<br>
      79288 Lindmoor<br>
      Fon: 0761 58 72 19<br>
      info@lindmoor-apotheke.example<br>
      www.lindmoor-apotheke.example
    </address>

    <div class="flyer__footer"></div>
  </main>
</body>
</html>
```